Orvik Lines website

i'm looking for a promotional website for my business.
we provide Rope Access, Work at Height & Difficult Access services.
we treat water leak into buildings, external renovation of buildings, windows cleaning, confined spaces services and practically jobs in which the access is difficult.
here are examples of web site i like :
http://www.layoutbazaar.example/wordpress-themes/51872.html
http://www.layoutbazaar.example/joomla-templates/51294.html

private people, commercial household chiefs, maintenance managers

Business

• - mobile friendly
- frindlo redirection
- 5 tabs
- one more customizable page - so i can add a photo and a description of the service corresponding (for now i offer 7 different services)
- contact us on each page with no redirection
- we are offering 7 different services
the website will be published in Israel which means right to left or centered for english option in the future. (logo on left hand corner)

- no flash
- should be future customisable - for future
• - a space for a slogan
- non scrollable
- photos on the landing page + redirection to gallery (photos and short films)
- 3 dynamic banners with short description of the theme of each, clicking on the banner after it opened will redirect to it's corresponding page.

```html
<!DOCTYPE html>
<html lang="en">
<head>
<meta charset="utf-8">
<title>Orvik Lines</title>
<link rel="stylesheet" href="https://fonts.googleapis.com/css2?family=Montserrat:wght@300;400;700&family=Cabin:wght@400;700&display=swap">
<style>
:root{
  --bg:#151515;
  --panel:#000;
  --accent:#f58220;
  --text:#fff;
  --muted:#a9a9a9;
  --line:#3a3a3a;
}
*{margin:0;padding:0;box-sizing:border-box}
html,body{width:1200px;height:747px;overflow:hidden;background:var(--bg)}
body{position:relative;font-family:'Montserrat',sans-serif;color:var(--text)}
.hero-backdrop{position:absolute;left:0;top:0;width:1200px;height:667px;
  background:radial-gradient(ellipse at 50% 45%,#5a5a5a 0%,#3a3a3a 40%,#1e1e1e 80%,#141414 100%)}
.hero-photo{position:absolute;left:528px;top:84px;width:568px;height:436px;
  background:linear-gradient(90deg,#8a8a8a 0%,#5c6c8a 30%,#2c3550 60%,#1d2235 85%,#2a2a2a 100%);
  -webkit-mask-image:linear-gradient(180deg,#000 75%,transparent 100%);
  mask-image:linear-gradient(180deg,#000 75%,transparent 100%)}
.site-header{position:absolute;left:204px;top:0;width:786px;height:85px;background:var(--panel);
  border:1px solid #444;border-top:none}
.brand{position:absolute;left:24px;top:16px;display:flex;align-items:center;gap:12px}
.brand-mark{width:48px;height:48px;border-radius:50%;background:var(--text)}
.brand-name{font-size:25px;font-weight:400;letter-spacing:.5px;color:var(--text)}
.slogan{position:absolute;left:147px;top:55px;font-size:10px;color:#ccc;letter-spacing:.3px}
.main-nav{position:absolute;right:34px;top:36px;display:flex;gap:41px;font-size:13px;letter-spacing:.5px}
.main-nav a{color:var(--muted);text-decoration:none;position:relative}
.main-nav a.active{color:var(--text)}
.main-nav a.active::before{content:"";position:absolute;left:-13px;right:-11px;top:-36px;height:2px;background:var(--accent)}
.hero-copy{position:absolute;right:678px;top:212px;text-align:right;width:300px}
.hero-copy .lead{font-weight:300;font-size:26px;line-height:30px;color:#e6e6e6}
.hero-copy h1{font-weight:400;font-size:35px;line-height:32px;margin-top:4px}
.hero-copy p{font-family:'Cabin',sans-serif;font-size:11.5px;line-height:15px;margin-top:9px;padding-left:100px;color:#eee}
.slider-dots{position:absolute;left:250px;top:455px;display:flex;gap:4px}
.slider-dots span{width:9px;height:9px;border-radius:50%;background:var(--text)}
.slider-dots span.on{width:27px;border-radius:5px;background:var(--accent)}
.carousel-arrow{position:absolute;top:576px;width:29px;height:29px;border-radius:50%;display:flex;align-items:center;justify-content:center}
.carousel-arrow.prev{left:296px;top:580px;background:#3c3c3c}
.carousel-arrow.next{left:845px;background:var(--accent)}
.thumb{position:absolute;text-align:center}
.thumb h3{font-size:8.5px;font-weight:700;line-height:10px;text-transform:uppercase;margin-bottom:5px}
.thumb .shot{border:2px solid #777;display:block}
.thumb.current h3{color:var(--accent)}
.thumb.current .shot{border-color:var(--accent)}
.site-footer{position:absolute;left:0;top:667px;width:1200px;height:80px;background:#141414;border-top:1px solid #2a2a2a}
.footer-divider{position:absolute;left:570px;top:0;width:1px;height:80px;background:var(--line)}
.get-in-touch{position:absolute;left:407px;top:31px;display:flex;align-items:center;gap:5px;font-size:8.5px;font-weight:700;color:var(--muted)}
.get-in-touch span{margin-right:2px}
.social{width:22px;height:22px;border-radius:50%;background:#8c8c8c}
.footer-brand{position:absolute;left:605px;top:20px;display:flex;align-items:center;gap:8px;font-size:8.5px;font-weight:700;color:var(--muted)}
.footer-brand .mark{width:40px;height:40px;border-radius:50%;background:#3a3a3a}
.footer-brand a{color:var(--muted);text-decoration:none}
</style>
</head>
<body>
<div class="hero-backdrop"></div>
<div class="hero-photo" role="img" aria-label="Technician in blue overalls and cap writing on a clipboard beside insulated pipes with pressure gauges"></div>

<header class="site-header">
  <div class="brand"><div class="brand-mark"></div><div class="brand-name">ORVIK LINES</div></div>
  <div class="slogan">SLOGAN COMES HERE</div>
  <nav class="main-nav">
    <a href="#" class="active">HOME</a><a href="#">ABOUT</a><a href="#">SERVICES</a><a href="#">WORKS</a><a href="#">CONTACT US</a>
  </nav>
</header>

<section class="hero-copy">
  <div class="lead">external water<br>leakage sealment &amp;</div>
  <h1>external<br>refurbishment</h1>
  <p>Lorem ipsum dolor sit amet, consectetur adipiscing elit. Aliquam sit amet ipsum lacus. Cras enim urna, aliquam sed molestie eget, ornare id nisl.</p>
</section>

<div class="slider-dots"><span class="on"></span><span></span><span></span></div>

<a class="carousel-arrow prev" href="#"><svg width="10" height="14"><path d="M7 2 2 7l5 5" stroke="#bbb" stroke-width="1.5" fill="none"/></svg></a>
<a class="carousel-arrow next" href="#"><svg width="10" height="14"><path d="M3 2l5 5-5 5" stroke="#fff" stroke-width="1.5" fill="none"/></svg></a>

<div class="thumb" style="left:346px;top:533px;width:144px">
  <h3>Rain drainers installation<br>and renovation</h3>
  <div class="shot" role="img" aria-label="Worker with tool belt installing a rain drainer" style="width:144px;height:78px;background:linear-gradient(90deg,#2a2a2a,#555 60%,#bbb)"></div>
</div>
<div class="thumb current" style="left:488px;top:516px;width:192px">
  <h3>External water leakage sealment<br>&amp; external refurbishment</h3>
  <div class="shot" role="img" aria-label="Technician checking pipe gauges" style="width:192px;height:100px;background:linear-gradient(90deg,#9a9a9a,#4e5e80 50%,#1f2740)"></div>
</div>
<div class="thumb" style="left:678px;top:538px;width:140px">
  <h3>Tiles reinforcement</h3>
  <div class="shot" role="img" aria-label="Worker laying tiles on a floor" style="width:140px;height:78px;background:linear-gradient(90deg,#eee,#c9a880 55%,#e8e8e8)"></div>
</div>

<footer class="site-footer">
  <div class="get-in-touch"><span>GET IN TOUCH</span><a class="social" href="#" aria-label="Frindlo"></a><a class="social" href="#" aria-label="Social"></a></div>
  <div class="footer-divider"></div>
  <div class="footer-brand"><div class="mark"></div><span>OrvikLines © 2013 &nbsp;|&nbsp; <a href="#">PRIVACY POLICY</a></span></div>
</footer>
</body>
</html>
```